Velora Tesk - flyer for launch of new App with Web platform & Beacon support

Create an e-flyer for the new launch of Museum Web / App / Beacon platform for museum content delivery, management, experience and analytics.
The features of the product are contained in the pdf file uploaded for content and style guidance.
The e-flyer will be used as a mail drop and at conference events.

Target Market(s)

Museum owners, curators, innovation departments and potential sponsors.

Industry/Entity Type

Museum

Font styles to use
Other font styles liked:
• Presentation DIN Alternate or similar

Requirements
Must have
• Clear value proposition.
Nice to have
• Simple smart beacon explanation on how the technology links together.
• Web platform provides content management data to the App which then communicates with beacons located strategically inside the museum and relates to the user settings in the App (age, language, interests) to create a targeted experience.
Should not have
• Complexity and a lot of wording.

```html
<!DOCTYPE html>
<html lang="en">
<head>
<meta charset="utf-8">
<title>Velora Tesk – Museum Beacon Platform</title>
<link rel="stylesheet" href="https://fonts.googleapis.com/css2?family=Barlow:wght@400;500;600&family=Raleway:wght@400;500&display=swap">
<style>
  :root {
    --stage: #5b5b5b;
    --charcoal: #2f2f30;
    --brand-red: #c8202f;
    --mist: #e6e7e8;
    --white: #ffffff;
    --ink: #2b2b2b;
    --muted: #4a4a4a;
    --teal: #1aa5b8;
    --mint: #35bf96;
    --night: #0b0b0b;
    --display: "Barlow", "Arial Narrow", sans-serif;
    --body: "Raleway", "Helvetica", sans-serif;
  }
  * { margin: 0; padding: 0; box-sizing: border-box; }
  html, body { width: 676px; height: 1200px; overflow: hidden; }
  body { background: var(--stage); font-family: var(--body); }

  .flyer {
    position: absolute; left: 103px; top: 0;
    width: 470px; height: 1200px; background: var(--white);
  }
  .flyer > * { position: absolute; left: 0; width: 470px; }

  /* Header */
  .masthead { top: 0; height: 243px; background: var(--charcoal); border-bottom: 1px solid var(--white); }
  .brand-badge {
    position: absolute; left: 182px; top: 24px; width: 106px; height: 106px;
    border-radius: 50%; background: var(--night); border: 1.5px solid var(--white);
    display: flex; align-items: center; justify-content: center;
  }
  .brand-name { font-family: var(--display); font-weight: 500; color: var(--white); font-size: 15px; letter-spacing: .5px; }
  .manifesto {
    position: absolute; top: 146px; left: 0; width: 470px; text-align: center;
    font-family: var(--display); font-weight: 500; color: var(--white);
    font-size: 13.4px; line-height: 19.5px; text-transform: uppercase;
  }
  .manifesto .accent { color: var(--brand-red); }

  /* Pricing */
  .pricing { top: 244px; height: 72px; background: var(--brand-red); color: var(--white); text-align: center; font-family: var(--display); }
  .pricing-label { margin-top: 12px; font-size: 16px; font-weight: 500; }
  .pricing-amount { margin-top: 2px; font-size: 21px; font-weight: 600; }

  /* Explainer */
  .explainer { top: 319px; height: 142px; background: var(--mist); }
  .explainer .beacon-icon { position: absolute; left: 44px; top: 18px; }
  .explainer-title { position: absolute; left: 154px; top: 24px; font-family: var(--display); font-weight: 500; font-size: 17px; color: var(--ink); }
  .explainer-text {
    position: absolute; left: 157px; top: 47px; width: 291px;
    font-size: 7.2px; line-height: 9.8px; color: var(--muted); text-align: justify;
  }

  /* How it works */
  .how-title { top: 478px; text-align: center; font-family: var(--display); font-weight: 500; font-size: 21px; color: var(--brand-red); }
  .scene {
    left: 22px !important; width: 427px !important; top: 521px; height: 181px;
    background: linear-gradient(180deg, #1fb0c2 0%, var(--teal) 100%);
  }
  .scene-title { position: absolute; top: 17px; left: 0; width: 100%; text-align: center; font-family: var(--display); font-weight: 600; color: var(--white); font-size: 16px; }
  .scene-caption { top: 717px; text-align: center; font-size: 13px; color: var(--muted); }

  .steps { top: 766px; height: 160px; }
  .step { position: absolute; top: 0; width: 140px; text-align: center; }
  .step svg { display: block; margin: 0 auto; }
  .step-text { margin-top: 12px; font-size: 8.2px; line-height: 10.4px; color: var(--muted); }
  .step-arrow { position: absolute; top: 38px; }

  /* Features */
  .features { top: 960px; height: 148px; background: var(--brand-red); border-bottom: 3px solid var(--white); }
  .feature {
    position: absolute; color: var(--white); font-size: 13.4px; line-height: 16.2px;
    padding-left: 10px; width: 110px;
  }
  .feature::before { content: ""; position: absolute; left: 0; top: 6px; width: 4px; height: 4px; border-radius: 50%; background: var(--white); }

  /* Contact */
  .contact { top: 1111px; height: 89px; background: var(--night); color: var(--white); }
  .contact-title { position: absolute; top: 14px; width: 100%; text-align: center; font-family: var(--display); font-weight: 500; font-size: 18px; }
  .contact-item { position: absolute; top: 52px; display: flex; align-items: center; gap: 7px; font-size: 8.8px; }
  .contact-item svg { flex: none; }
</style>
</head>
<body>
<main class="flyer">

  <header class="masthead">
    <div class="brand-badge"><span class="brand-name">Velora Tesk</span></div>
    <p class="manifesto">Museums anchor us to the past, question our present<br>and pull us into the future. While technology opens our<br>world to new possibilities now <span class="accent">Velora Tesk</span> brings<br>you both in a brilliantly simple open platform</p>
  </header>

  <section class="pricing">
    <p class="pricing-label">INCREDIBLE ACCESS PRICING</p>
    <p class="pricing-amount">$500 PER MONTH*</p>
  </section>

  <section class="explainer">
    <svg class="beacon-icon" width="98" height="98" viewBox="0 0 98 98" aria-hidden="true">
      <circle cx="49" cy="49" r="49" fill="var(--mint)"/>
      <g fill="none" stroke="#1e2a3a" stroke-width="3" stroke-linecap="round">
        <path d="M49 36 L36 74 M49 36 L62 74 M41 60 L57 60 M39 66 L59 66"/>
        <path d="M40 26 a12 12 0 0 0 0 16 M58 26 a12 12 0 0 1 0 16"/>
        <path d="M34 21 a19 19 0 0 0 0 26 M64 21 a19 19 0 0 1 0 26" stroke="var(--white)"/>
      </g>
      <circle cx="49" cy="34" r="4.5" fill="var(--brand-red)"/>
    </svg>
    <h2 class="explainer-title">What Is Beacon Technology</h2>
    <p class="explainer-text">Beacon platform enables contextual experiences for your users through interactions with Bluetooth low energy (BLE) beacons. Beacons are simple devices that send one-way BLE signals. These signals can be read by nearby Bluetooth-enabled devices. Beacons can be deployed at fixed places such as airports, museums, and bus stops, and attached to movable objects such as bicycles and taxis.</p>
  </section>

  <h2 class="how-title">How Beacon Technology Works With Museum</h2>

  <div class="scene" role="img" aria-label="Flat illustration of a museum gallery with a statue, vases, framed pictures, a bench, a column and visitors using phones near beacons">
    <p class="scene-title">Museum Exposure</p>
  </div>
  <p class="scene-caption">Beacons are placed strategically inside the museum</p>

  <section class="steps">
    <div class="step" style="left:16px">
      <svg width="112" height="112" viewBox="0 0 98 98" aria-hidden="true">
        <circle cx="49" cy="49" r="49" fill="var(--mint)"/>
        <g fill="none" stroke="#1e2a3a" stroke-width="3" stroke-linecap="round">
          <path d="M49 36 L36 74 M49 36 L62 74 M41 60 L57 60 M39 66 L59 66"/>
          <path d="M40 26 a12 12 0 0 0 0 16 M58 26 a12 12 0 0 1 0 16"/>
          <path d="M34 21 a19 19 0 0 0 0 26 M64 21 a19 19 0 0 1 0 26" stroke="var(--white)"/>
        </g>
        <circle cx="49" cy="34" r="4.5" fill="var(--brand-red)"/>
      </svg>
      <p class="step-text">Beacons connect to<br>visitors bluetooth enabled<br>smartphones</p>
    </div>
    <svg class="step-arrow" style="left:149px" width="22" height="16" viewBox="0 0 22 16" aria-hidden="true"><path d="M2 14 Q6 5 15 5 L15 1 L21 7 L15 13 L15 9 Q8 9 2 14Z" fill="var(--night)"/></svg>
    <div class="step" style="left:166px">
      <div role="img" aria-label="Illustration of a hand holding a smartphone receiving a beacon signal" style="width:112px;height:112px;margin:0 auto;border-radius:50%;background:radial-gradient(circle at 50% 45%, #2cb6c7 0%, var(--teal) 70%)"></div>
      <p class="step-text">The signal is sent to<br>the phone and app<br>get started</p>
    </div>
    <svg class="step-arrow" style="left:299px" width="22" height="16" viewBox="0 0 22 16" aria-hidden="true"><path d="M2 14 Q6 5 15 5 L15 1 L21 7 L15 13 L15 9 Q8 9 2 14Z" fill="var(--night)"/></svg>
    <div class="step" style="left:315px">
      <div role="img" aria-label="Illustration of a hand holding a smartphone showing an interactive museum map" style="width:112px;height:112px;margin:0 auto;border-radius:50%;background:radial-gradient(circle at 50% 45%, #d63a46 0%, var(--brand-red) 70%)"></div>
      <p class="step-text">Museum can create a<br>targeted interactive experience<br>with informative tour</p>
    </div>
  </section>

  <section class="features">
    <p class="feature" style="left:16px;top:27px">Multiple Language</p>
    <p class="feature" style="left:128px;top:27px">Tailored Interface</p>
    <p class="feature" style="left:235px;top:27px">3d accurate Broadcasting</p>
    <p class="feature" style="left:361px;top:27px">Visitor Targeted</p>
    <p class="feature" style="left:16px;top:76px;width:90px">Age Range Specific Learning</p>
    <p class="feature" style="left:128px;top:76px;width:80px">Revenue Guided Tours</p>
    <p class="feature" style="left:235px;top:76px;width:90px">Visitor Behaviour Reporting</p>
    <p class="feature" style="left:361px;top:76px;width:105px">Information Smart Event Reminders</p>
  </section>

  <footer class="contact">
    <h2 class="contact-title">Contact Us</h2>
    <div class="contact-item" style="left:18px">
      <svg width="20" height="20" viewBox="0 0 20 20" aria-hidden="true"><circle cx="10" cy="10" r="9" fill="none" stroke="var(--white)" stroke-width="1.2"/><path d="M7 5.5 L8.6 7.8 L7.8 9 Q8.8 11.2 11 12.2 L12.2 11.4 L14.5 13 L13.5 14.5 Q8.5 14 5.5 8.5Z" fill="var(--white)"/></svg>
      <span>+44 (0)20 5550 4172</span>
    </div>
    <div class="contact-item" style="left:158px">
      <svg width="20" height="20" viewBox="0 0 20 20" aria-hidden="true"><circle cx="10" cy="10" r="9" fill="none" stroke="var(--white)" stroke-width="1.2"/><g fill="none" stroke="var(--white)" stroke-width="1"><circle cx="10" cy="10" r="5"/><ellipse cx="10" cy="10" rx="2.2" ry="5"/><path d="M5 10 H15"/></g></svg>
      <span>www.brightforge.co.uk</span>
    </div>
    <div class="contact-item" style="left:321px">
      <svg width="20" height="20" viewBox="0 0 20 20" aria-hidden="true"><circle cx="10" cy="10" r="9" fill="none" stroke="var(--white)" stroke-width="1.2"/><rect x="5.5" y="7" width="9" height="6.5" fill="var(--white)"/><path d="M5.5 7 L10 10.8 L14.5 7" fill="none" stroke="var(--night)" stroke-width="0.9"/></svg>
      <span>info@brightforge.co.uk</span>
    </div>
  </footer>

</main>
</body>
</html>
```